Pagecraft Design for Fruit & Veggie Swap Site

I need a pagecraft design for the HOME PAGE of a company located in Kona, Hawaii called Leafway Exchange Hawaii. Leafway Exchange Hawaii (LEH) is a site intended to support the local food movement by connecting neighbors in order for them to swap/trade produce from their farm or garden. The purpose of this site is to support sustainable agriculture in Hawaii and encourage community interaction.

The model of the site is similar to:
http://www.harvtrade.me/ (I really like the simple design of this site)
http://www.plotbarter.co.uk/ (I don't like the design of this site, just the functionality. The design is too busy and unbalanced.)
Unlike the two sites listed above, however, LEH is only targeted at people living on the Big Island of Hawaii.

The site is simply intended to be a platform to connect people, then they are free to swap or barter off site, similar to the way postboardly connects people. Users can create "posts" for crops that they have available for swap, which are searchable based on name and location.

I have created a very basic, no-css, dev version of the site to work on the back end, which is located here: http://leafwayexchangehawaii.com/test
Feel free to register and create a test post to get a feel for how it works.

The images I have uploaded are just for ideas and do not have to be in the design.

Target Market(s)

The targeted audience is gardeners and farmers on the Big Island of Hawaii. These people are quite varied in age and technical ability.

Industry/Entity Type

Agriculture

Requirements
Must have
• On the homepage, I would like to have a list of the most recent "posts", displayed as the post title, with the most recent post at the top of the list. In the test site, this is located in the right column, but it doesn't have to be in that location in the final design.

I would also like the option to "Add new listing" to be displayed creatively on the home page. This can be in the form of a graphic that links to a form on another page.

I would also like to have a search box on the homepage. Users can search by crop name and/or location.

The main focal point of the home page will be a Mapsly map application of the Big Island. I am in the process of developing this. You can see the map on the test site, please keep in mind that this map may change slightly in future revisions. Feel free to change the size and styling of the map to fit your design.

I would like the homepage to have a simple and clean layout, making it clear to users how the site works.
For the graphics, I would like to incorporate the "crop circles" idea (yes, like the alien crop circles in fields) with fruits and veggies (including tropical fruit found in Hawaii like banana, coconut, lychee, taro, oranges, as well as traditional vegetables like carrots, lettuce, etc.), and also potentially with the idea of sharing and circulating produce with neighbors.
Please note that those specific fruits and veggies don't need to be used, or that many of them, I was just giving them as examples.

I would also like to have a place on the homepage where users can login/sign up. This can be a login form with a sign up link, or a login link and a sign up link.

I would like the entire design to fit on a page without having to scroll.

Once the site has a substantial user base, I plan to incorporate advertising. Please create a design that will be easy to integrate ads into in the future, most likely in the side bar or footer. I do not want the original design to have ad space, just the ability to add it easily in the future and having it look good with the current design.

```html
<!DOCTYPE html>
<html lang="en">
<head>
<meta charset="utf-8">
<title>Leafway Exchange Hawaii</title>
<link rel="stylesheet" href="https://fonts.googleapis.com/css2?family=Oswald:wght@400;500&display=swap">
<style>
  :root {
    --bg: #000000;
    --leaf-dark: #1f5a12;
    --leaf-mid: #3d7f22;
    --leaf-bright: #3ea617;
    --panel-green: rgba(88, 178, 50, 0.82);
    --tile-green: rgba(96, 190, 56, 0.78);
    --accent-lime: #9ccf3c;
    --white: #ffffff;
    --red: #c8102e;
    --olive: #c2b400;
    --blue: #3a6db5;
    --cyan: #1e9fd6;
    --search-bg: #f2f2f2;
    --search-text: #4a5570;
    --map-water: #a7bfdd;
    --map-land: #eceae3;
  }
  * { box-sizing: border-box; margin: 0; padding: 0; }
  html, body { width: 1200px; height: 900px; overflow: hidden; background: var(--bg); }
  body { position: relative; font-family: "Oswald", sans-serif; color: var(--white); }

  .top-tab { position: absolute; left: 180px; top: 152px; width: 132px; height: 8px; background: #141a10; }

  .stage {
    position: absolute; left: 88px; top: 159px; width: 1024px; height: 513px;
    background: radial-gradient(ellipse at 30% 40%, #4f8f2a 0%, var(--leaf-mid) 40%, var(--leaf-dark) 100%);
  }

  .brand-mark { position: absolute; left: 180px; top: 182px; width: 130px; text-align: center; }
  .brand-mark .dot { width: 62px; height: 62px; border-radius: 50%; background: var(--accent-lime); margin: 0 auto 6px; }
  .brand-mark .name { font-size: 12px; letter-spacing: 1px; text-transform: uppercase; line-height: 1.2; }

  .search { position: absolute; left: 124px; top: 304px; width: 240px; height: 34px; display: flex; }
  .search .field { flex: 1; background: var(--search-bg); color: var(--search-text); font-size: 20px; font-weight: 500; padding: 2px 9px; line-height: 30px; }
  .search .go { width: 30px; background: var(--cyan); display: flex; align-items: center; justify-content: center; }

  .nav { position: absolute; top: 362px; height: 27px; font-size: 14px; line-height: 27px; text-align: center; text-transform: uppercase; }
  .nav-how { left: 96px; width: 91px; background: var(--red); }
  .nav-faq { left: 193px; width: 93px; background: var(--olive); }
  .nav-contact { left: 291px; width: 89px; background: var(--blue); }

  .account-bar { position: absolute; left: 72px; top: 412px; width: 318px; height: 47px; background: var(--leaf-bright);
    display: flex; align-items: center; padding-left: 76px; gap: 34px; font-size: 14px; letter-spacing: 4px; }
  .account-bar span { display: flex; align-items: center; gap: 9px; }

  .new-post { position: absolute; left: 115px; top: 460px; width: 274px; height: 185px; border-radius: 0 0 4px 4px;
    background: linear-gradient(135deg, #8a6a3a, #5e8a2e 45%, #a3422e 100%); overflow: hidden; }
  .new-post .overlay { position: absolute; left: 0; top: 10px; width: 265px; height: 172px; background: var(--tile-green); }
  .new-post .bars { position: absolute; left: 32px; top: 58px; width: 79px; }
  .new-post .bars i { display: block; height: 10px; background: var(--white); margin-bottom: 12px; }
  .new-post .label { position: absolute; left: 145px; top: 52px; font-size: 30px; line-height: 30px; font-weight: 400; }

  .site-title { position: absolute; left: 418px; top: 196px; font-size: 38px; font-weight: 400; line-height: 56px; white-space: nowrap;
    text-shadow: 2px 2px 3px rgba(0,0,0,0.45); }
  .site-title .place { color: var(--accent-lime); font-size: 26px; margin-left: 6px; }
  .tagline { position: absolute; left: 418px; top: 258px; font-size: 17px; letter-spacing: 0.3px; text-transform: uppercase; }

  .map { position: absolute; left: 417px; top: 303px; width: 393px; height: 343px;
    background: radial-gradient(ellipse at 55% 55%, var(--map-land) 0%, #d9e6c8 40%, var(--map-water) 70%); }

  .recent-heading { position: absolute; left: 857px; top: 203px; font-size: 22px; letter-spacing: 6px; text-transform: uppercase;
    border-bottom: 1px solid var(--white); line-height: 28px; }
  .recent-panel { position: absolute; left: 833px; top: 254px; width: 258px; height: 378px; background: var(--panel-green); padding: 20px 16px 0 25px; }
  .recent-panel li { list-style: none; font-size: 13px; line-height: 24px; }

  .all-link { position: absolute; left: 1022px; top: 645px; width: 94px; height: 27px; background: var(--leaf-bright);
    font-size: 13px; letter-spacing: 3px; text-align: center; line-height: 27px; }
</style>
</head>
<body>
  <div class="top-tab"></div>
  <div class="stage" role="img" aria-label="Background photo collage of tropical fruit and leafy greens"></div>

  <div class="brand-mark">
    <div class="dot"></div>
    <div class="name">Leafway Exchange Hawaii</div>
  </div>

  <div class="search">
    <div class="field">search for...</div>
    <div class="go">
      <svg width="16" height="16" viewBox="0 0 16 16"><circle cx="6" cy="6" r="4.5" fill="none" stroke="#fff" stroke-width="2"/><line x1="9.5" y1="9.5" x2="14.5" y2="14.5" stroke="#fff" stroke-width="3" stroke-linecap="round"/></svg>
    </div>
  </div>

  <div class="nav nav-how">How it works</div>
  <div class="nav nav-faq">FAQ</div>
  <div class="nav nav-contact">Contact</div>

  <div class="account-bar">
    <span><svg width="16" height="16" viewBox="0 0 16 16"><circle cx="8" cy="4.5" r="4" fill="#fff"/><path d="M0 16 C0 9 16 9 16 16 Z" fill="#fff"/></svg>LOGIN</span>
    <span><svg width="12" height="12" viewBox="0 0 12 12"><rect x="4" y="0" width="4" height="12" fill="#fff"/><rect x="0" y="4" width="12" height="4" fill="#fff"/></svg>REGISTER</span>
  </div>

  <div class="new-post" role="img" aria-label="Photo of fresh produce behind the new post button">
    <div class="overlay">
      <div class="bars"><i></i><i></i><i></i></div>
      <div class="label">NEW<br>POST</div>
    </div>
  </div>

  <h1 class="site-title">LEAFWAY EXCHANGE<span class="place">HAWAII</span></h1>
  <p class="tagline">Conecting neighbours for local food exchange</p>

  <div class="map" role="img" aria-label="Interactive map of the Big Island of Hawaii with pins marking produce posts"></div>

  <h2 class="recent-heading">Recent posts</h2>
  <ul class="recent-panel">
    <li>testing redirect 3 (Honaunau)</li>
    <li>testing redirect 2 (Honaunau)</li>
    <li>testing redirect (Volcano)</li>
    <li>Testing no street address (Milolii)</li>
    <li>Lemons (Pahala)</li>
    <li>Oranges (Kohala)</li>
    <li>Coconuts (hilo)</li>
    <li>Lettuce (Holualoa)</li>
    <li>Testuser trying to add photo (Hawi)</li>
    <li>New post from testuser with map and photo (honokaa)</li>
    <li>New post from testuser (honokaa)</li>
    <li>Papaya seedlings (captain cook)</li>
  </ul>

  <div class="all-link">&lsaquo; ALL &rsaquo;</div>
</body>
</html>
```